Design a Logo for Wine Label

Hello,
We're looking for a new wine label design for our 2015 vintage. We would like a cross section of both traditional and modern styles.
The name is Kellmoor Ridge Shiraz, feel free to incorporate that into the design if you will.
It would be preferable to be a Front and Back Label. Front would have the design element and the back label should have space for ingredients and other mandated health information.
A quick search would come up with results. I have intentionally not uploaded an existing label as I want a fresh look.
Thank you

```html
<!DOCTYPE html>
<html lang="en">
<head>
<meta charset="utf-8">
<title>Kellmoor Ridge Shiraz – Front Label</title>
<link rel="stylesheet" href="https://fonts.googleapis.com/css2?family=Caveat:wght@500&family=Raleway:wght@300&display=swap">
<style>
  :root {
    --backdrop: #f4f1ec;
    --label-cream: #efe5d6;
    --wine-text: #7b2743;
    --ink-soft: #4d4040;
    --ridge-dark: #4a1e2a;
    --ridge-mid: #a8452a;
    --ridge-warm: #e0762f;
    --ridge-light: #efe9e6;
    --grape-deep: #3c4a78;
    --grape-mid: #5d6fa6;
  }
  html, body {
    margin: 0;
    width: 1200px;
    height: 1035px;
    overflow: hidden;
    background: var(--backdrop);
  }
  .label {
    position: absolute;
    left: 360px;
    top: 47px;
    width: 480px;
    height: 940px;
    background: var(--label-cream);
    overflow: hidden;
    box-shadow: 0 2px 10px rgba(0,0,0,0.08);
  }
  .ridge-art {
    position: absolute;
    left: 0; top: 0;
    width: 100%;
    height: 345px;
    background:
      radial-gradient(ellipse 55% 30% at 55% 20%, var(--ridge-light) 0%, rgba(239,233,230,0) 100%),
      linear-gradient(180deg, var(--ridge-dark) 0%, #7a3a3a 40%, var(--ridge-mid) 70%, var(--ridge-warm) 90%, rgba(224,118,47,0) 100%);
  }
  .wine-name {
    position: absolute;
    left: 0; right: 0;
    top: 405px;
    margin: 0;
    text-align: center;
    font-family: "Caveat", cursive;
    font-weight: 500;
    font-size: 56px;
    color: var(--wine-text);
    white-space: nowrap;
  }
  .grape-art {
    position: absolute;
    left: 112px;
    top: 540px;
    width: 265px;
    height: 320px;
    border-radius: 45% 45% 50% 50% / 30% 30% 70% 70%;
    background: radial-gradient(ellipse at 45% 35%, var(--grape-mid) 0%, var(--grape-deep) 100%);
  }
  .corner-art {
    position: absolute;
    left: 0;
    bottom: 0;
    width: 110px;
    height: 175px;
    background: linear-gradient(160deg, var(--ridge-warm) 0%, var(--ridge-mid) 50%, var(--ridge-dark) 100%);
    clip-path: polygon(0 0, 100% 100%, 0 100%);
  }
  .label-details {
    position: absolute;
    bottom: 20px;
    left: 140px;
    right: 50px;
    display: flex;
    justify-content: space-between;
    font-family: "Raleway", sans-serif;
    font-weight: 300;
    font-size: 38px;
    color: var(--ink-soft);
  }
</style>
</head>
<body>
  <main class="label">
    <div class="ridge-art" role="img" aria-label="Low-poly mountain ridge illustration in plum, rust and orange tones"></div>
    <h1 class="wine-name">Kellmoor Ridge Shiraz</h1>
    <div class="grape-art" role="img" aria-label="Low-poly illustration of a bunch of dark blue grapes"></div>
    <div class="corner-art" role="img" aria-label="Low-poly corner ornament in warm tones"></div>
    <div class="label-details">
      <span class="vintage">2015</span>
      <span class="volume">750ml</span>
    </div>
  </main>
</body>
</html>
```